Varnek Group Business Card

Varnek Group — Business Card Design Brief
Overview
Design a double-sided business card for Varnek Group that highlights our two service arms: Varnek Communications (telecommunications) and Varnek Energy (business energy solutions). The card should feel smart and stand out when handed to clients.

Objectives
Showcase our areas of specialty clearly.
Reflect the overall Varnek / Varnek Group brand while acknowledging both arms.
Explore using both logos (Communications + Energy) or one unified logo, depending on the design.

Deliverables
One double-sided business card design (front + back).

Content & Copy
Front (preferred): Logo: Varnek / Varnek Group
Descriptor: Business Communications | Business Energy
Back:My contact details and company details
Core products: Business Mobile • Telephony • Internet • Business Energy Solutions

Brand & Visual Direction
We have a group logo currently tailored more toward telecoms, plus a separate Varnek Energy logo.
Please explore layouts that use both logos or just one, whichever works best.
Color: I wouldn't mind seeing an option using our the Blue/Purple gradient from our website (varnek-example.co.uk), but also open to non-gradient approaches and other colours..

Overall look: Smart, modern, and distinctive.
Format & Print Specs
Double-sided business card format. (Use a standard size

Must-Haves
Front: Varnek wording or Varnek Group wording with atleast 1 logo also on front “Business Communications | Business Energy.”

Back: Contact + company details and core products.
A design that stands out while remaining professional.

Nice-to-Have Options
A gradient version using our site’s Blue/Purple gradient.
A non-gradient version.
A dual-logo treatment versus a single-logo treatment.

Thanks
Dominic

```html
<!DOCTYPE html>
<html lang="en">
<head>
<meta charset="utf-8">
<title>Varnek Group Business Card</title>
<link rel="stylesheet" href="https://fonts.googleapis.com/css2?family=Montserrat:wght@400;600;700&family=Poppins:wght@800&display=swap">
<style>
  :root {
    --backdrop: #979797;
    --purple: #84449a;
    --blue: #1067a8;
    --navy: #1c3263;
    --ink-navy: #2a1f5e;
    --ink: #111111;
    --text: #2b2b2b;
    --accent: #1a9ad6;
    --brand-blue: #3d6bbd;
    --brand-green: #38a84a;
    --white: #ffffff;
  }
  * { margin: 0; padding: 0; box-sizing: border-box; }
  html, body { width: 1200px; height: 1108px; overflow: hidden; }
  body { background: var(--backdrop); position: relative; font-family: "Montserrat", sans-serif; }

  .card { position: absolute; left: 242px; width: 715px; height: 409px; border-radius: 36px; overflow: hidden; }

  .card-front {
    top: 119px;
    background: linear-gradient(122deg, var(--purple) 0%, var(--purple) 38%, var(--blue) 56%, var(--navy) 70%, var(--navy) 100%);
  }
  .front-mark { position: absolute; left: 0; right: 0; top: 104px; display: flex; flex-direction: column; align-items: center; }
  .front-mark .dot { width: 112px; height: 112px; border-radius: 50%; background: var(--brand-green); }
  .front-mark .wordmark {
    margin-top: 22px; font-family: "Poppins", sans-serif; font-weight: 800;
    font-size: 64px; line-height: 1; letter-spacing: 1px; color: var(--ink-navy);
  }
  .descriptor {
    margin-top: 8px; font-size: 14px; font-weight: 600; letter-spacing: 1.5px;
    color: var(--white); text-transform: uppercase;
  }
  .services {
    position: absolute; left: 0; right: 0; top: 353px; text-align: center;
    font-size: 19px; font-weight: 400; color: var(--white); letter-spacing: 0.3px;
  }

  .card-back { top: 581px; background: var(--white); }
  .back-mark { position: absolute; left: 0; right: 0; top: 26px; display: flex; flex-direction: column; align-items: center; }
  .back-mark .dot { width: 100px; height: 100px; border-radius: 50%; background: var(--brand-blue); }
  .back-mark .wordmark {
    margin-top: 14px; font-family: "Poppins", sans-serif; font-weight: 800;
    color: var(--ink); text-align: center; line-height: 1;
  }
  .wordmark .name { display: block; font-size: 52px; }
  .wordmark .arm { display: block; font-size: 17px; letter-spacing: 3px; margin-top: 4px; }

  .person { position: absolute; right: 411px; top: 256px; text-align: right; }
  .person .full-name { font-weight: 700; font-size: 36px; color: var(--text); line-height: 1.1; }
  .person .role { font-size: 19px; color: var(--text); margin-top: 6px; }

  .divider { position: absolute; left: 340px; top: 241px; width: 2px; height: 102px; background: var(--accent); }

  .contacts { position: absolute; left: 374px; top: 236px; list-style: none; }
  .contacts li { display: flex; align-items: center; height: 28.5px; font-size: 19px; color: var(--text); }
  .contacts svg { width: 16px; height: 16px; margin-right: 9px; fill: var(--accent); flex: none; }

  .address { position: absolute; left: 0; right: 0; top: 362px; text-align: center; font-size: 19px; color: var(--text); }
</style>
</head>
<body>
  <section class="card card-front">
    <div class="front-mark">
      <div class="dot"></div>
      <div class="wordmark">VARNEK</div>
      <p class="descriptor">Business Communications | Business Energy</p>
    </div>
    <p class="services">Business Mobile • Telephony • Internet • Business Energy Solutions</p>
  </section>

  <section class="card card-back">
    <div class="back-mark">
      <div class="dot"></div>
      <div class="wordmark"><span class="name">VARNEK</span><span class="arm">COMMUNICATIONS</span></div>
    </div>

    <div class="person">
      <p class="full-name">Owen Radley</p>
      <p class="role">Managing Director</p>
    </div>

    <div class="divider"></div>

    <ul class="contacts">
      <li><svg viewBox="0 0 24 24"><path d="M6.6 10.8a15 15 0 0 0 6.6 6.6l2.2-2.2a1 1 0 0 1 1-.25 11.4 11.4 0 0 0 3.6.57 1 1 0 0 1 1 1V20a1 1 0 0 1-1 1A17 17 0 0 1 3 4a1 1 0 0 1 1-1h3.5a1 1 0 0 1 1 1c0 1.250.2 2.45.57 3.57a1 1 0 0 1-.25 1z"/></svg>+44 0161 555 0142</li>
      <li><svg viewBox="0 0 24 24"><path d="M12 2a10 10 0 0 0-8.6 15.1L2 22l5-1.3A10 10 0 1 0 12 2zm0 18a8 8 0 0 1-4.1-1.1l-.3-.2-3 .8.8-2.9-.2-.3A8 8 0 1 1 12 20zm4.4-6c-.2-.1-1.4-.7-1.6-.8s-.4-.1-.5.1-.6.8-.7.9-.3.2-.5.1a6.5 6.5 0 0 1-3.2-2.8c-.2-.4.2-.4.7-1.2a.4.4 0 0 0 0-.4l-.7-1.7c-.2-.5-.4-.4-.5-.4h-.5a.9.9 0 0 0-.6.3 2.7 2.7 0 0 0-.8 2 4.6 4.6 0 0 0 1 2.5 10.6 10.6 0 0 0 4 3.6c1.5.6 2.1.7 2.8.6a2.4 2.4 0 0 0 1.6-1.1 2 2 0 0 0 .1-1.1c0-.2-.2-.2-.6-.4z"/></svg>+44 7700 900 318 (Live Chat)</li>
      <li><svg viewBox="0 0 24 24"><path d="M2 5h20v14H2zm2 2v.4l8 5.2 8-5.2V7l-8 5.2z"/></svg>info@varnek-example.co.uk</li>
      <li><svg viewBox="0 0 24 24"><path d="M12 2a10 10 0 1 0 0 20 10 10 0 0 0 0-20zm-1 17.9A8 8 0 0 1 4.2 10L9 14.8v1a2 2 0 0 0 2 2zm6.9-2.5a2 2 0 0 0-1.9-1.4h-1v-3a1 1 0 0 0-1-1H8v-2h2a1 1 0 0 0 1-1V7h2a2 2 0 0 0 2-2v-.4a8 8 0 0 1 2.9 12.8z"/></svg>varnek-example.co.uk</li>
    </ul>

    <p class="address">24 Harlow Lane, Manchester, England, M1 7QT</p>
  </section>
</body>
</html>
```